Corporate Identity Design Project

Marisol Tevendry Design is a small boutique event planning and floral design company, based in Northern Alberta. I require the creation of some corporate identity pieces. I want a minimalistic design.
Website www.marisoltevendry.com

Pieces should include
1. Business Card
Should include the company logo, name, email address, address, phone number. These will be professional printed.
These are three cards that I like:
http://cardlayoutgallerynook.com/wp-content/uploads/2010/02/Renata_Voskuilen_Roomworks_by_Pepperleaf_studio_Graphics.jpg
http://tidycardshowcase.com/wp-content/uploads/2011/06/Quietfold-Studio-Minimalist-Business-Cards_11.jpg
http://graphiclanternhub.com/wp-content/uploads/2012/03/16.minimalist-business-cards.jpg
I like letterpress, but I am open to other options.

2. Letterhead
will be professionally printed

3. Envelope

4. Fax Sheet
will be printed on home printer

5. Pocket Presentation
Like -http://fernwickgardenworks.com/img/design_step_proposal@2x.jpg

6. Invoice
Like - http://velmaquorlin.files.blogsite-example.com/2011/02/summit-strength-4-letterhead-combined.png?w=529

7. Proposal
Like something like this – this will not be printed, but rather emailed to clients
Like http://getfile7.brindlepost.com/getfile/files.brindlepost.com/tarnu-studio/qwRtZe8MmXp3LoKcV7B2nhdYJsaWeFUy6gT4rkPHvxiQbNcDzA9jsLE/Picture-52.png.scaled.500.jpg

8. Contract
Like http://www.brightkeelpromo.co.uk/images/tamsin-contract.jpg

9. Business Brochure – I have removed this piece from the project and will most likely post it as another project at a later date.

If you think that this is a project of interest to you, but feel that it is “too much” work for the price, please let me know how you would re-package it – I am open to suggestions.

Target Market(s)

Young women

Industry/Entity Type

Boutique

Requirements
Should not have
• I do not want it to look "frilly"

```html
<!DOCTYPE html>
<html lang="en">
<head>
<meta charset="utf-8">
<title>Marisol Tevendry Design — Business Card</title>
<link rel="stylesheet" href="https://fonts.googleapis.com/css2?family=Montserrat:wght@500&display=swap">
<style>
  :root {
    --backdrop: #e9e6e2;
    --card-black: #040404;
    --pattern-deep: #0b0b0b;
    --pattern-mid: #171615;
    --pattern-light: #252322;
    --mark-grey: #cfcfcf;
  }
  * { margin: 0; padding: 0; box-sizing: border-box; }
  html, body {
    width: 1200px;
    height: 796px;
    overflow: hidden;
    background: var(--backdrop);
  }
  .canvas {
    position: relative;
    width: 1200px;
    height: 796px;
  }
  .business-card {
    position: absolute;
    left: 250px;
    top: 188px;
    width: 700px;
    height: 420px;
    background: var(--card-black);
    border-radius: 52px 52px 0 52px;
    overflow: hidden;
    box-shadow: 0 6px 18px rgba(0, 0, 0, 0.25);
  }
  .card-pattern {
    position: absolute;
    inset: 0;
    background:
      radial-gradient(circle at 18% 22%, var(--pattern-light) 0%, transparent 18%),
      radial-gradient(circle at 42% 12%, var(--pattern-mid) 0%, transparent 20%),
      radial-gradient(circle at 66% 20%, var(--pattern-light) 0%, transparent 16%),
      radial-gradient(circle at 88% 30%, var(--pattern-mid) 0%, transparent 18%),
      radial-gradient(circle at 12% 62%, var(--pattern-mid) 0%, transparent 20%),
      radial-gradient(circle at 34% 48%, var(--pattern-light) 0%, transparent 17%),
      radial-gradient(circle at 56% 72%, var(--pattern-mid) 0%, transparent 18%),
      radial-gradient(circle at 24% 88%, var(--pattern-light) 0%, transparent 16%),
      radial-gradient(circle at 80% 86%, var(--pattern-mid) 0%, transparent 16%),
      linear-gradient(160deg, var(--pattern-deep), var(--card-black) 70%);
  }
  .brand-lockup {
    position: absolute;
    left: 352px;
    top: 200px;
    display: flex;
    align-items: center;
    gap: 18px;
  }
  .brand-dot {
    width: 50px;
    height: 50px;
    border-radius: 50%;
    background: var(--mark-grey);
    flex: none;
  }
  .brand-name {
    font-family: "Montserrat", sans-serif;
    font-weight: 500;
    font-size: 23px;
    line-height: 1.12;
    letter-spacing: 0.14em;
    color: var(--mark-grey);
  }
  .brand-name .line { display: block; }
  .brand-name .caps { text-transform: uppercase; }
</style>
</head>
<body>
  <main class="canvas">
    <section class="business-card">
      <div class="card-pattern" role="img" aria-label="Dark tonal floral damask pattern of scrolls and leaves covering the card"></div>
      <div class="brand-lockup">
        <span class="brand-dot"></span>
        <p class="brand-name">
          <span class="line caps">Marisol</span>
          <span class="line caps">Tevendry</span>
          <span class="line">design</span>
        </p>
      </div>
    </section>
  </main>
</body>
</html>
```